PELDRAX Business Cards

We require a business card for our company that provides IT consulting services. We already have a logo that needs to be used on the card. We want a clean professional looking design that incorporates our colours. Our main focus is providing managed services to business, which involves us looking after all of their IT requirements including managing servers/networks, projects, and procurement.

Industry/Entity Type

Information Technology

Requirements
Must have
• our logo, contact information, name, title, phone numbers

```html
<!DOCTYPE html>
<html lang="en">
<head>
<meta charset="utf-8">
<title>PELDRAX Business Cards</title>
<link rel="stylesheet" href="https://fonts.googleapis.com/css2?family=Montserrat:wght@500;600;700&display=swap">
<style>
  :root {
    --page: #ffffff;
    --card-blue: #1593d1;
    --ink-white: #ffffff;
  }
  * { margin: 0; padding: 0; box-sizing: border-box; }
  html, body {
    width: 1200px; height: 1200px; overflow: hidden;
    background: var(--page);
    font-family: "Montserrat", sans-serif;
    color: var(--ink-white);
  }
  .canvas { position: relative; width: 1200px; height: 1200px; }
  .card {
    position: absolute; top: 456px;
    width: 506px; height: 287px;
    background: var(--card-blue);
    overflow: hidden;
  }
  .card--front { left: 86px; }
  .card--back { left: 617px; }

  .rule { position: absolute; height: 9px; }
  .rule::before, .rule::after {
    content: ""; position: absolute; left: 0; right: 0; background: var(--ink-white);
  }
  .rule::before { top: 0; height: 2px; }
  .rule::after { top: 6px; height: 3px; }
  .rule--left { left: 0; width: 152px; top: 139px; }
  .rule--right { left: 350px; width: 156px; top: 139px; }

  .front-name {
    position: absolute; left: 152px; width: 198px; top: 126px;
    text-align: center;
    font-weight: 600; font-size: 26px; letter-spacing: 1px; line-height: 34px;
  }

  .back-name {
    position: absolute; left: 46px; top: 38px;
    font-weight: 600; font-size: 30px; letter-spacing: 1px; line-height: 36px;
  }

  .contact {
    position: absolute; left: 354px; top: 270px;
    transform: rotate(-90deg); transform-origin: top left;
    white-space: nowrap; text-transform: uppercase;
  }
  .contact__person { font-weight: 700; font-size: 17px; letter-spacing: 1px; line-height: 19px; }
  .contact__title { font-weight: 600; font-size: 8px; letter-spacing: 0.5px; line-height: 12px; margin-bottom: 10px; }
  .contact__list { list-style: none; font-weight: 600; font-size: 11px; letter-spacing: 0.8px; line-height: 16px; }
  .contact__label { display: inline-block; width: 20px; }
  .contact__indent { padding-left: 20px; }
</style>
</head>
<body>
<main class="canvas">
  <section class="card card--front" aria-label="Card front">
    <div class="rule rule--left"></div>
    <div class="front-name">PELDRAX</div>
    <div class="rule rule--right"></div>
  </section>

  <section class="card card--back" aria-label="Card back">
    <div class="back-name">PELDRAX</div>
    <div class="contact">
      <div class="contact__person">Mara Lenski</div>
      <div class="contact__title">Director</div>
      <ul class="contact__list">
        <li><span class="contact__label">P.</span>+ 001 555 789</li>
        <li><span class="contact__label">E.</span>info@peldrax.com</li>
        <li><span class="contact__label">W.</span>www.peldrax.com</li>
        <li><span class="contact__label">A.</span>Alder Brook Road Fenwick</li>
        <li class="contact__indent">FW Northshire</li>
      </ul>
    </div>
  </section>
</main>
</body>
</html>
```